Asia Hotel need a card and logo

The new hotel in East Asia, Taiwan need a business card and logo design.The hotel's Chinese name is 岚柏文旅,English name is "Velmira Hotel".The core concept of this hotel is "Eco green", going to use many plant etc.,The building's first outlook draft is attached in the file for your reference.The style be modern and fashion will be good. Thank you.
Target Market(s)
East Asia
Industry/Entity Type
Hotel
Contact Information for Business Card
The hotel's name both in Chinese and English :岚柏商旅 Velmira Hotel
The logo, address, E-mail and tel number place.
Stuff's name and title.
Font styles to use
Colors
Designer to choose colors to be used in the design.
Look and feel
Each slider illustrates characteristics of the customer's brand and the style your logo design should communicate.

```html
<!DOCTYPE html>
<html lang="en">
<head>
<meta charset="utf-8">
<title>Velmira Hotel – Business Card</title>
<link href="https://fonts.googleapis.com/css2?family=Jost:wght@300&family=Arimo:wght@400;700&family=Noto+Sans+SC:wght@300&display=swap" rel="stylesheet">
<style>
  :root {
    --backdrop: #e6e5e3;
    --sage: #8b9873;
    --sage-text: #8a9a6a;
    --paper: #f5f5f2;
    --ink: #3a3a3a;
    --wordmark-grey: #7c7c7c;
    --frame-line: #f3f3ef;
  }
  * { margin: 0; padding: 0; box-sizing: border-box; }
  html, body { width: 1200px; height: 1000px; overflow: hidden; }
  body {
    background: var(--backdrop);
    display: flex;
    align-items: center;
    justify-content: center;
    gap: 90px;
    font-family: "Arimo", Arial, sans-serif;
  }
  .card {
    position: relative;
    width: 400px;
    height: 660px;
    box-shadow: 0 6px 18px rgba(0,0,0,0.12);
  }

  /* Front */
  .card--front { background: var(--sage); color: var(--frame-line); }
  .card__frame {
    position: absolute;
    inset: 22px;
    border: 1.5px solid var(--frame-line);
  }
  .brand-mark {
    position: absolute;
    left: 50%;
    transform: translateX(-50%);
    width: 46px;
    height: 46px;
    border-radius: 50%;
  }
  .card--front .brand-mark { top: 262px; border: 2px solid var(--frame-line); }
  .wordmark {
    position: absolute;
    left: 0; right: 0;
    text-align: center;
    font-family: "Jost", sans-serif;
    font-weight: 300;
    letter-spacing: 0.32em;
    text-transform: uppercase;
  }
  .wordmark__cn {
    display: block;
    font-family: "Noto Sans SC", sans-serif;
    font-weight: 300;
    letter-spacing: 0.15em;
    text-transform: none;
  }
  .card--front .wordmark { bottom: 58px; font-size: 17px; }
  .card--front .wordmark__cn { font-size: 12px; margin-top: 4px; }

  /* Back */
  .card--back { background: var(--paper); color: var(--ink); }
  .card--back .brand-mark { top: 190px; width: 34px; height: 34px; border: 2px solid var(--sage-text); }
  .card--back .wordmark { top: 246px; font-size: 15px; color: var(--wordmark-grey); }
  .card--back .wordmark__cn { font-size: 11px; margin-top: 3px; }

  .contact {
    position: absolute;
    left: 40px;
    top: 440px;
    font-size: 15px;
    line-height: 1.3;
  }
  .contact__name { font-size: 16px; }
  .contact__title { color: var(--sage-text); font-weight: 700; font-size: 14px; }
  .contact__list { list-style: none; margin-top: 20px; }
  .contact__list li { display: flex; }
  .contact__label { color: var(--sage-text); width: 26px; }
  .contact__address { margin-top: 16px; font-style: normal; }
</style>
</head>
<body>
  <section class="card card--front" aria-label="Card front">
    <div class="card__frame"></div>
    <span class="brand-mark"></span>
    <p class="wordmark">Velmira Hotel<span class="wordmark__cn">岚柏商旅</span></p>
  </section>

  <section class="card card--back" aria-label="Card back">
    <span class="brand-mark"></span>
    <p class="wordmark">Velmira Hotel<span class="wordmark__cn">岚柏商旅</span></p>

    <div class="contact">
      <p class="contact__name">Stuff's Name</p>
      <p class="contact__title">Title</p>
      <ul class="contact__list">
        <li><span class="contact__label">T:</span>1-888-555-0142</li>
        <li><span class="contact__label">E:</span>stay@velmirahotel.com</li>
        <li><span class="contact__label">W:</span>www.velmirahotel.com</li>
      </ul>
      <address class="contact__address">
        No. 27, Section 1,<br>
        Hesong Road, Zhongshan District,<br>
        Taipei City, Taiwan 104
      </address>
    </div>
  </section>
</body>
</html>
```